Uprising SaaS company needs an attractive business card design

We're an uprising SaaS company who's attempting to attack the rigid car (insurance) claims management market in Europe.
We want to our mighty base order management system, listen to our clients to connect the smart ideas to build something even mightier.
We primarily focus on helping our customers manage their customers' claims/orders and get them resolved as smoothly as possible.
We'd like the business card design to express technical innovation and the fact that we connect smart ideas, as our company slogan indicates.
Contact Information for Business Card
Name, position, website, email, mobile, business address
Font styles to use
Colors
Designer to choose colors to be used in the design.
Look and feel
Each slider illustrates characteristics of the customer's brand and the style your logo design should communicate.

```html
<!DOCTYPE html>
<html lang="en">
<head>
<meta charset="utf-8">
<title>Veltrano business card</title>
<link href="https://fonts.googleapis.com/css2?family=Montserrat:wght@300;500&display=swap" rel="stylesheet">
<style>
  :root {
    --backdrop: #e6eaec;
    --cream: #fdf8ec;
    --sky: #84d0e6;
    --slate: #7e7f80;
    --ink: #7a7a7a;
    --accent: #7ccbe3;
  }
  html, body {
    margin: 0;
    padding: 0;
    width: 1200px;
    height: 1000px;
    overflow: hidden;
    background: var(--backdrop);
    font-family: "Montserrat", Arial, sans-serif;
  }
  .canvas { position: relative; width: 1200px; height: 1000px; }
  .card {
    position: absolute;
    border-radius: 28px;
    overflow: hidden;
    background: var(--cream);
    box-shadow: 0 8px 20px rgba(0,0,0,0.12);
  }
  .card-shapes { position: absolute; inset: 0; }
  .card-front { left: 375px; top: 55px; width: 690px; height: 442px; }
  .card-back  { left: 135px; top: 528px; width: 695px; height: 444px; }
  .text { position: absolute; margin: 0; white-space: nowrap; color: var(--ink); font-weight: 300; }
  .person-name { left: 227px; top: 50px; font-size: 31px; line-height: 1; }
  .person-name .given { font-weight: 500; }
  .person-role { left: 227px; top: 90px; font-size: 24px; line-height: 1; }
  .wordmark { color: var(--ink); font-weight: 300; letter-spacing: 1px; }
  .card-front .wordmark { left: 52px; top: 236px; font-size: 54px; line-height: 1; }
  .phone { left: 452px; top: 242px; font-size: 20px; color: var(--accent); display: flex; align-items: center; gap: 4px; }
  .contact-row { position: absolute; left: 55px; top: 356px; display: flex; align-items: center; color: var(--ink); font-weight: 300; font-size: 19px; }
  .contact-row .email { display: flex; align-items: center; gap: 8px; }
  .contact-row .divider { width: 1.5px; height: 40px; background: var(--ink); margin: 0 12px; }
  .contact-row .address { display: flex; align-items: center; gap: 12px; line-height: 1.25; }
  .ghost-name { left: 118px; top: 62px; font-size: 112px; line-height: 1; color: rgba(255,255,255,0.2); letter-spacing: 2px; }
  .card-back .wordmark { left: 48px; top: 314px; font-size: 70px; line-height: 1; }
  .website { left: 487px; top: 235px; font-size: 21px; color: var(--accent); }
  svg.icon { fill: none; stroke: currentColor; stroke-width: 1.6; }
</style>
</head>
<body>
<main class="canvas">

  <section class="card card-front" aria-label="Card front">
    <svg class="card-shapes" width="690" height="442" viewBox="0 0 690 442">
      <polygon points="0,0 625,0 420,269" fill="var(--sky)"/>
      <polygon points="625,0 690,0 690,442 420,269" fill="var(--slate)"/>
    </svg>
    <p class="text person-name"><span class="given">Jonas</span> Keller</p>
    <p class="text person-role">CEO</p>
    <p class="text wordmark">veltrano</p>
    <p class="text phone">
      <svg class="icon" width="18" height="18" viewBox="0 0 24 24"><path d="M5 3h4l2 5-2.5 1.5a11 11 0 0 0 6 6L16 13l5 2v4a2 2 0 0 1-2 2A16 16 0 0 1 3 5a2 2 0 0 1 2-2z"/></svg>+49 170 5550142
    </p>
    <div class="contact-row">
      <span class="email">
        <svg class="icon" width="18" height="14" viewBox="0 0 18 14"><rect x="1" y="1" width="16" height="12"/><path d="M1 1l8 6 8-6"/></svg>info@veltrano.com
      </span>
      <span class="divider"></span>
      <span class="address">
        <svg class="icon" width="14" height="18" viewBox="0 0 14 18"><path d="M7 17s6-6 6-10A6 6 0 0 0 1 7c0 4 6 10 6 10z"/><circle cx="7" cy="7" r="2"/></svg>
        <span>Lindenweg 14b<br>10115 Berlin - Germany</span>
      </span>
    </div>
  </section>

  <section class="card card-back" aria-label="Card back">
    <svg class="card-shapes" width="695" height="444" viewBox="0 0 695 444">
      <polygon points="15,0 675,0 420,272" fill="var(--sky)"/>
      <polygon points="675,0 695,0 695,444 420,272" fill="var(--slate)"/>
    </svg>
    <p class="text ghost-name">veltrano</p>
    <p class="text website">veltrano.com</p>
    <p class="text wordmark">veltrano</p>
  </section>

</main>
</body>
</html>
```